Design 6.5 x 9 Postcard for Business

You will need to design a 6.5" x 9" postcard for our insulation business, Brightfold Energy, LLC based on design requirements. We will be using PostRiver and have attached template for guide. Must include phone number, web address, company logo, warm haven partner logo and marketing call to action. Specificallyl marketing 75-100% off insulation & weatheriation services with FREE Home Energy Assessment. Absolutely no cost. I have given examples of other companies on attachment as well for inspiration. I will also need to ensure that somewhere clear is "Our company just insulated a home on your mail route and we'd like to offer you a FREE assessment!"

Here are competitior websites for inspiration.

https://www.lumatekpower.example/?gclid=XbTqRwLmPz8KdYhNvCu3-FJe2WQSaLpOkMxGyH_ZtUeR

https://www.tidalnestpower.example/

```html
<!DOCTYPE html>
<html lang="en">
<head>
<meta charset="utf-8">
<title>Brightfold Energy Postcard</title>
<link rel="stylesheet" href="https://fonts.googleapis.com/css2?family=Montserrat:wght@400;500;600;700;800;900&family=Roboto+Condensed:ital,wght@1,500&display=swap">
<style>
  :root{
    --navy:#1f4f8a;
    --navy-deep:#1a4577;
    --green:#4f9a36;
    --green-bright:#5fb043;
    --brown:#5b3a22;
    --ink:#2b2b2b;
    --sky:#4aa9d9;
    --white:#ffffff;
    --bg:#e9ece9;
  }
  *{margin:0;padding:0;box-sizing:border-box}
  html,body{width:1197px;height:1200px;overflow:hidden;background:var(--bg);font-family:"Montserrat",sans-serif;color:var(--ink)}
  .postcard{position:absolute;left:208px;width:780px;height:563px;background:var(--white);overflow:hidden;box-shadow:0 4px 14px rgba(0,0,0,.15)}
  .postcard--front{top:24px}
  .postcard--back{top:613px}
  .abs{position:absolute}

  /* brand */
  .brand{display:flex;align-items:center;gap:10px}
  .brand__square{width:30px;height:30px;background:var(--navy)}
  .brand__name{font-weight:700;font-size:24px;color:var(--navy);letter-spacing:.2px}

  /* front */
  .front__photo{left:300px;top:0;width:480px;height:450px;
    background:linear-gradient(160deg,#9cc4e4 0%,#d9d2c0 35%,#c99a5c 60%,#6a5a44 85%,#3e6f8a 100%);
    clip-path:polygon(14% 0,100% 0,100% 100%,0 100%,0 30%)}
  .front__topband{right:0;top:0;width:420px;height:34px;background:var(--brown);clip-path:polygon(6% 0,100% 0,100% 100%,0 100%);
    color:var(--white);font-size:12px;font-weight:600;display:flex;align-items:center;justify-content:flex-end;padding-right:22px;gap:6px}
  .front__logo{left:34px;top:48px}
  .headline{left:34px;top:150px;width:460px}
  .headline__intro{font-weight:800;font-size:24px;line-height:1.15;color:var(--ink)}
  .headline__offer{display:inline-block;margin-top:8px;background:var(--green-bright);color:var(--white);font-weight:900;font-size:44px;padding:2px 14px;line-height:1.1}
  .headline__with{margin-top:8px;display:flex;align-items:center;gap:10px;font-weight:800;font-size:24px}
  .headline__free{background:var(--green-bright);color:var(--white);font-weight:900;font-size:38px;padding:0 12px;line-height:1.15}
  .headline__assess{margin-top:6px;font-weight:800;font-size:24px}
  .headline__nocost{display:inline-block;margin-top:6px;background:var(--brown);color:var(--white);font-weight:800;font-size:21px;padding:5px 14px}
  .front__footer{left:0;bottom:0;width:780px;height:112px;background:var(--navy);
    display:flex;align-items:center;color:var(--white)}
  .footer__address{width:330px;padding-left:40px;font-size:14px;font-weight:500;line-height:1.45;display:flex;gap:8px}
  .footer__divider{width:1px;height:56px;background:rgba(255,255,255,.6);margin:0 28px}
  .footer__contact{font-size:14px;line-height:1.5}
  .footer__contact .phone{font-size:24px;font-weight:800;font-style:italic}
  .partner-badge{right:36px;top:330px;width:150px;height:150px;border-radius:50%;background:var(--white);display:flex;align-items:center;justify-content:center;box-shadow:0 2px 6px rgba(0,0,0,.15)}
  .partner-badge__shape{width:90px;height:60px;border-radius:10px;background:var(--green)}
  .icon{display:inline-block;vertical-align:middle}

  /* back */
  .back__logo{right:34px;top:26px}
  .back__partner{left:330px;top:56px;width:90px;height:50px;border-radius:8px;background:var(--green)}
  .back__green{left:0;top:110px;width:480px;height:194px;background:var(--green);clip-path:polygon(0 24%,72% 0,100% 0,100% 100%,0 100%)}
  .back__message{left:30px;top:166px;color:var(--white)}
  .back__message p{font-size:17px;font-weight:500;line-height:1.22}
  .back__message strong{display:block;margin-top:4px;font-size:30px;font-weight:900;letter-spacing:.5px;line-height:1.15}
  .back__phone{left:500px;top:128px;display:flex;align-items:center;gap:12px;font-weight:900;font-size:30px;color:#111}
  .back__phone .phone-dot{width:40px;height:40px;border-radius:50%;background:var(--sky);display:flex;align-items:center;justify-content:center}
  .back__band{left:0;top:304px;width:780px;height:30px;background:var(--navy);color:var(--white);
    font-family:"Roboto Condensed",sans-serif;font-style:italic;font-weight:500;font-size:15.5px;display:flex;align-items:center;padding-left:24px}
  .services{left:24px;top:350px;display:flex;gap:30px}
  .service{display:flex;align-items:center;gap:10px;font-size:13px;font-weight:600;line-height:1.15}
  .service__icon{width:44px;height:44px;border-radius:50%;background:var(--sky);display:flex;align-items:center;justify-content:center}
  .about{left:24px;top:418px;width:440px}
  .about__title{font-size:19px;font-weight:700;color:var(--ink);padding-bottom:4px;border-bottom:1px solid var(--brown);display:inline-block}
  .about__title span{color:var(--navy)}
  .about__text{margin-top:6px;font-size:8px;line-height:1.4;color:#444}
  .back__footer{left:0;bottom:0;width:470px;height:70px;background:var(--navy-deep);clip-path:polygon(0 0,94% 0,100% 100%,0 100%);color:var(--white);display:flex;align-items:center}
  .back__footer .footer__address{width:220px;padding-left:24px;font-size:11px}
  .back__footer .footer__divider{height:40px;margin:0 18px}
  .back__footer .footer__contact{font-size:11px;line-height:1.45}
  .indicia{right:30px;top:350px;width:66px;height:52px;border:1px solid #666;font-size:6px;line-height:1.35;text-align:center;padding-top:6px;color:#333}
  .mailing{left:520px;top:448px;width:230px}
  .mailing__code{font-size:7px;text-align:right;color:#333}
  .mailing__line{border-top:2px dotted #555;margin:4px 0}
  .mailing__to{font-size:8px;color:#333}
</style>
</head>
<body>

<section class="postcard postcard--front">
  <div class="abs front__photo" role="img" aria-label="Photo of a modern two-storey home with warm lit windows, wood slat accents and a pool at dusk"></div>
  <div class="abs front__topband">
    <svg class="icon" width="12" height="12" viewBox="0 0 12 12"><circle cx="6" cy="6" r="5" fill="none" stroke="#fff" stroke-width="1.3"/><path d="M1 6h10M6 1c2 2 2 8 0 10M6 1c-2 2-2 8 0 10" fill="none" stroke="#fff" stroke-width="1"/></svg>
    www.brightfoldenergy.example
  </div>

  <div class="abs brand front__logo">
    <span class="brand__square"></span>
    <span class="brand__name">Brightfold Energy</span>
  </div>

  <div class="abs headline">
    <div class="headline__intro">Insulation and<br>Weatherization Services</div>
    <div class="headline__offer">75-100% OFF</div>
    <div class="headline__with">with <span class="headline__free">FREE</span></div>
    <div class="headline__assess">Home Energy Assessment</div>
    <div class="headline__nocost">at ABSOLUTELY NO COST</div>
  </div>

  <div class="abs partner-badge"><span class="partner-badge__shape"></span></div>

  <div class="abs front__footer">
    <div class="footer__address">
      <svg class="icon" width="12" height="16" viewBox="0 0 12 16"><path d="M6 1a5 5 0 0 1 5 5c0 4-5 9-5 9S1 10 1 6a5 5 0 0 1 5-5z" fill="#8fd16f"/><circle cx="6" cy="6" r="2" fill="#1f4f8a"/></svg>
      <span>42 Harbor Lane, Suite B2,<br>Fairhaven Point, MA 02999</span>
    </div>
    <div class="footer__divider"></div>
    <div class="footer__contact">
      <div>
        <svg class="icon" width="14" height="10" viewBox="0 0 14 10"><rect x="1" y="1" width="12" height="8" fill="none" stroke="#8fd16f" stroke-width="1.2"/><path d="M1 1l6 5 6-5" fill="none" stroke="#8fd16f" stroke-width="1.2"/></svg>
        info@brightfoldenergy.example
      </div>
      <div class="phone">
        <svg class="icon" width="16" height="16" viewBox="0 0 16 16"><circle cx="8" cy="8" r="7" fill="none" stroke="#8fd16f" stroke-width="1.4"/><path d="M5.5 4.5l1.5 1.5-1 1c.6 1.2 1.5 2.1 2.7 2.7l1-1 1.5 1.5-1 1.2c-2.8-.5-5.2-2.9-5.7-5.7z" fill="#8fd16f"/></svg>
        555-014-2290
      </div>
    </div>
  </div>
</section>

<section class="postcard postcard--back">
  <div class="abs brand back__logo">
    <span class="brand__square"></span>
    <span class="brand__name">Brightfold Energy</span>
  </div>
  <div class="abs back__partner"></div>

  <div class="abs back__green"></div>
  <div class="abs back__phone">
    <span class="phone-dot"><svg width="20" height="20" viewBox="0 0 16 16"><path d="M4 2.5l2.2 2.2-1.3 1.4c.8 1.7 2.1 3 3.8 3.8l1.4-1.3 2.2 2.2-1.5 1.7C7 12 3.9 9 3.3 5z" fill="#fff"/></svg></span>
    555-014-2290
  </div>
  <div class="abs back__message">
    <p>Our company<br>Just insulated a home<br>on your mail route<br>and we'd like to offer you a</p>
    <strong>FREE ASSESSMENT!</strong>
  </div>

  <div class="abs back__band">Following the assessment, we will make suggestions to improve its energy efficiency including but not limited to:</div>

  <div class="abs services">
    <div class="service">
      <span class="service__icon"><svg width="24" height="24" viewBox="0 0 24 24"><rect x="3" y="5" width="18" height="14" fill="none" stroke="#fff" stroke-width="1.6"/><path d="M3 12h18M9 5v7M15 12v7" stroke="#fff" stroke-width="1.6"/></svg></span>
      <span>Wall<br>Insulation</span>
    </div>
    <div class="service">
      <span class="service__icon"><svg width="24" height="24" viewBox="0 0 24 24"><rect x="7" y="3" width="10" height="18" fill="none" stroke="#fff" stroke-width="1.6"/><circle cx="14" cy="12" r="1.2" fill="#fff"/></svg></span>
      <span>General<br>Construction</span>
    </div>
    <div class="service">
      <span class="service__icon"><svg width="24" height="24" viewBox="0 0 24 24"><path d="M3 12l9-8 9 8M6 10v10h12V10" fill="none" stroke="#fff" stroke-width="1.6"/><rect x="10" y="13" width="4" height="4" fill="none" stroke="#fff" stroke-width="1.4"/></svg></span>
      <span>Attic<br>Insulation</span>
    </div>
    <div class="service">
      <span class="service__icon"><svg width="24" height="24" viewBox="0 0 24 24"><path d="M3 9h12a3 3 0 1 0-3-3M3 13h16a3 3 0 1 1-3 3M3 17h8" fill="none" stroke="#fff" stroke-width="1.6" stroke-linecap="round"/></svg></span>
      <span>Air<br>Sealing</span>
    </div>
  </div>

  <div class="abs indicia">PRSRT STD<br>ECRWSS<br>U.S. POSTAGE<br>PAID<br>EDDM RETAIL</div>

  <div class="abs about">
    <div class="about__title">About <span>Brightfold Energy</span></div>
    <p class="about__text">Brightfold Energy is a small, locally owned business in Fairhaven Point, Massachusetts. If you're a homeowner, commercial or residential landlord, we provide a solution to reduce your energy costs, both heating and electrical. We provide a free, no-obligation assessment for your home.</p>
  </div>

  <div class="abs mailing">
    <div class="mailing__code">ECRWSS</div>
    <div class="mailing__line"></div>
    <div class="mailing__to">Local<br>Postal Customer</div>
  </div>

  <div class="abs back__footer">
    <div class="footer__address">
      <svg class="icon" width="10" height="14" viewBox="0 0 12 16"><path d="M6 1a5 5 0 0 1 5 5c0 4-5 9-5 9S1 10 1 6a5 5 0 0 1 5-5z" fill="#fff"/></svg>
      <span>42 Harbor Lane, Suite B2,<br>Fairhaven Point, MA 02999</span>
    </div>
    <div class="footer__divider"></div>
    <div class="footer__contact">
      <div>info@brightfoldenergy.example</div>
      <div>555-014-2290</div>
      <div>www.brightfoldenergy.example</div>
    </div>
  </div>
</section>

</body>
</html>
```